Kem7Dex Letterhead

Need a new letterhead for my law firm.
IDENTIFYING INFORMATION BELOW:
Ansel T Brightwater III
Attorney at Law
Address: 4832 Tillbury Rd, Ste 250, Dallas, TX 75204
Phone: 866-402-7183
Fax: 469-583-0271
Email: kem@kem7dex.example
Website: www.kem7dex.example

Colors
0054AA
0677BA
7BADD7
CADEEF
E8F1F8

Requirements
Must have
• Logo needs to be on the letterhead, along with identifying information which is included in the project description.

```html
<!DOCTYPE html>
<html lang="en">
<head>
<meta charset="utf-8">
<title>Kem7Dex Letterhead</title>
<link rel="stylesheet" href="https://fonts.googleapis.com/css2?family=Montserrat:wght@300;400;500;600&display=swap">
<style>
  :root {
    --blue-deep: #0054AA;
    --blue-mid: #0677BA;
    --blue-soft: #7BADD7;
    --blue-pale: #CADEEF;
    --blue-mist: #E8F1F8;
    --ink: #333638;
    --ink-soft: #6b6f73;
    --backdrop: #ececec;
    --paper: #ffffff;
  }
  * { box-sizing: border-box; margin: 0; padding: 0; }
  html, body { width: 1200px; height: 900px; overflow: hidden; }
  body {
    background: var(--backdrop);
    font-family: "Montserrat", Arial, sans-serif;
    color: var(--ink);
  }
  .letterhead {
    position: absolute;
    left: 275px; top: 30px;
    width: 650px; height: 840px;
    background: var(--paper);
    box-shadow: 0 6px 24px rgba(0,0,0,0.12);
    overflow: hidden;
  }
  .accent-band {
    position: absolute;
    left: 0; top: 0;
    width: 70px; height: 195px;
    background: radial-gradient(circle at 60% 45%, #2aa6e0 0%, var(--blue-mid) 45%, var(--blue-deep) 100%);
  }
  .accent-block {
    position: absolute;
    right: 0; bottom: 0;
    width: 160px; height: 190px;
    background: radial-gradient(circle at 40% 40%, #2aa6e0 0%, var(--blue-mid) 40%, var(--blue-deep) 100%);
  }
  .brand {
    position: absolute;
    left: 112px; top: 40px;
  }
  .brand-line {
    display: flex;
    align-items: center;
    gap: 10px;
  }
  .brand-square {
    width: 14px; height: 14px;
    background: var(--blue-mid);
  }
  .brand-name {
    font-weight: 500;
    font-size: 28px;
    letter-spacing: 0.5px;
    line-height: 1;
    color: var(--ink);
  }
  .brand-tagline {
    margin-top: 7px;
    font-weight: 300;
    font-size: 10.5px;
    letter-spacing: 2.4px;
    color: var(--ink-soft);
    text-transform: uppercase;
  }
  .contact-card {
    position: absolute;
    left: 415px; top: 38px;
    padding-left: 10px;
    border-left: 2px solid var(--blue-mid);
  }
  .contact-name {
    font-weight: 600;
    font-size: 14px;
    color: var(--ink);
  }
  .contact-title {
    font-size: 9.5px;
    color: var(--blue-mid);
    margin-bottom: 12px;
  }
  .contact-list { list-style: none; }
  .contact-list li {
    display: flex;
    align-items: flex-start;
    gap: 6px;
    font-size: 8.5px;
    line-height: 1.35;
    color: var(--ink-soft);
    margin-bottom: 2px;
  }
  .contact-list .address { margin-bottom: 10px; }
  .contact-list svg {
    flex: none;
    width: 9px; height: 9px;
    margin-top: 1px;
    fill: var(--blue-mid);
  }
  .contact-list .line-icon { fill: none; stroke: var(--blue-mid); stroke-width: 0.9; }
</style>
</head>
<body>
  <main class="letterhead">
    <div class="accent-band"></div>

    <header class="brand">
      <div class="brand-line">
        <span class="brand-square"></span>
        <span class="brand-name">Kem7Dex</span>
      </div>
      <div class="brand-tagline">Counsel you can keep</div>
    </header>

    <section class="contact-card">
      <div class="contact-name">Ansel T Brightwater III</div>
      <div class="contact-title">Attorney at Law</div>
      <ul class="contact-list">
        <li class="address">
          <svg viewBox="0 0 10 10"><path d="M5 0C3 0 1.6 1.5 1.6 3.4 1.6 6 5 10 5 10s3.4-4 3.4-6.6C8.4 1.5 7 0 5 0zm0 4.7a1.3 1.3 0 1 1 0-2.6 1.3 1.3 0 0 1 0 2.6z"/></svg>
          <span>4832 Tillbury Rd, Ste 250,<br>Dallas, TX 75204</span>
        </li>
        <li>
          <svg viewBox="0 0 10 10"><path d="M2.2 0.5l1.6 2.2-1 1.1c.6 1.3 1.6 2.3 2.9 2.9l1.1-1 2.2 1.6-.9 2.1C4 9.2.8 6 .1 1.4z"/></svg>
          <span>866-402-7183</span>
        </li>
        <li>
          <svg viewBox="0 0 10 10"><path d="M2.5 0h5v2.8h-5zM0.5 3.5h9v4h-2v2.5h-5V7.5h-2zM3.3 6.5v2.7h3.4V6.5z"/></svg>
          <span>469-583-0271</span>
        </li>
        <li>
          <svg viewBox="0 0 10 10"><g class="line-icon"><path d="M0.5 2h9v6h-9z"/><path d="M0.8 2.6L5 5.6l4.2-3"/></g></svg>
          <span>kem@kem7dex.example</span>
        </li>
        <li>
          <svg viewBox="0 0 10 10"><g class="line-icon"><circle cx="5" cy="5" r="4.4"/><ellipse cx="5" cy="5" rx="2" ry="4.4"/><path d="M0.6 5h8.8"/></g></svg>
          <span>www.kem7dex.example</span>
        </li>
      </ul>
    </section>

    <div class="accent-block"></div>
  </main>
</body>
</html>
```